Financial services referral site needs a redesign

We need a complete re-brand ; new word press design for our existing site. Need a web 2.0 clean crisp look that will convert highly. Consumers with debt come to our site so we can refer them to 3rd party providers of debt solutions ranging from credit counseling, debt consolidation, refinance and student loan consolidation. I would like to see designs that use the color green and final product should communicate safety, trust and privacy. Show case our A+ QFR rating etc. See current site at pinegroveloanaid.com

- I would like to use light blue color scheme to match the logo. The green is making it look off - I definitely need the lead form to be on the top right side of the page

```html
<!DOCTYPE html>
<html lang="en">
<head>
<meta charset="utf-8">
<title>Pine Grove Loan Aid</title>
<link href="https://fonts.googleapis.com/css2?family=Open+Sans:ital,wght@0,400;0,600;0,700;1,400&display=swap" rel="stylesheet">
<style>
:root{
  --brand:#1a7fc1;
  --blue:#0b7bd0;
  --blue-dark:#0a6ab5;
  --teal-top:#6ea3ad;
  --teal-bot:#2f6a77;
  --red:#b5103c;
  --ink:#222;
  --muted:#555;
  --card-line:#cfe3ea;
  --footer:#d9d6d8;
}
*{box-sizing:border-box;margin:0;padding:0}
html,body{width:952px;height:1200px;overflow:hidden;background:#fff}
body{font-family:'Open Sans',sans-serif;color:var(--ink);position:relative}
.abs{position:absolute}

.brand{left:100px;top:22px;display:flex;align-items:center;gap:10px}
.brand-dot{width:42px;height:42px;border-radius:50%;background:#8ec9d6}
.brand-name{font-size:19px;font-weight:400;color:var(--brand);letter-spacing:-.2px}

.top-contact{right:100px;top:20px;text-align:right}
.top-contact .label{font-size:14px;color:#333;display:flex;align-items:center;justify-content:flex-end;gap:6px}
.top-contact .phone{font-size:16px;color:#111;margin-top:2px;letter-spacing:.3px}

.nav{left:100px;top:95px;width:752px;height:38px;background:linear-gradient(var(--teal-top),var(--teal-bot));border-radius:2px;display:flex;align-items:center;padding-left:11px}
.nav a{color:#fff;text-decoration:none;font-size:16px;font-weight:600;margin-right:29px}
.nav a.active{color:#b9ecf5}
.login{position:absolute;right:5px;top:8px;width:71px;height:22px;background:#fff;border:1px solid #aaa;font-size:12px;color:#333;display:flex;align-items:center;gap:6px;padding-left:8px}

.hero{left:100px;top:152px;width:496px;height:292px;background:linear-gradient(135deg,#7f8a97,#b9a892 45%,#4b5566)}
.hero-shadow{left:104px;top:444px;width:488px;height:16px;background:radial-gradient(ellipse at top,rgba(0,0,0,.18),transparent 70%)}
.hero-dots{left:122px;top:423px;width:36px;height:10px;background:#fff;border-radius:5px;display:flex;justify-content:space-around;align-items:center;padding:0 3px}
.hero-dots i{width:4px;height:4px;border-radius:50%;background:#555}
.hero-dots i.on{background:var(--red)}

.lead{left:602px;top:144px;width:241px;height:300px;background:var(--blue)}
.lead-tab{left:596px;top:144px}
.lead h2{font-size:17px;font-weight:600;color:#fff;text-align:center;line-height:24px;margin-top:22px}
.lead hr{border:0;border-top:1px dashed #f2a3a3;margin:12px 24px 0}
.field{position:absolute;height:23px;background:#fff;font-size:9px;font-style:italic;color:#444;padding:6px 8px}
.field .caret{position:absolute;right:8px;top:9px;width:0;height:0;border-left:4px solid transparent;border-right:4px solid transparent;border-top:5px solid #222}
.cta{position:absolute;left:27px;top:218px;width:189px;height:30px;background:var(--red);border-bottom:2px solid #7d0a29;color:#fff;font-size:13px;font-weight:600;text-align:center;line-height:29px;border-radius:2px}

.card{top:502px;width:241px;height:160px;border:2px solid var(--card-line);background:#fff}
.card-shadow{top:662px;width:241px;height:10px;background:radial-gradient(ellipse at top,rgba(0,0,0,.16),transparent 70%)}
.card h3{font-size:13px;font-weight:400;color:var(--brand);text-align:center;line-height:18px;margin-top:8px}
.benefits{list-style:none;margin:20px 0 0 22px;font-size:10px;color:#222}
.benefits li{line-height:17.6px;display:flex;align-items:center;gap:4px}
.news{position:absolute;left:10px;width:220px;display:flex;gap:12px}
.news .date{width:20px;font-size:8px;text-align:center}
.news .date b{display:block;margin-top:3px;background:var(--red);color:#fff;font-size:8px;font-weight:700;height:12px;line-height:12px}
.news .t{font-size:7.5px;color:#222;margin-bottom:5px}
.news p{font-size:6px;color:#555;line-height:9.6px}
.news p span{color:var(--red)}
.articles{margin:14px 0 0 18px;font-size:8px;color:#333;line-height:17.6px;padding-right:8px}
.see-more{position:absolute;left:20px;top:131px;width:53px;height:18px;background:var(--blue);color:#fff;font-size:8px;font-weight:600;text-align:center;line-height:18px}

.intro{left:101px;top:736px;width:460px}
.intro h2{font-size:18px;font-weight:400;color:#111;margin-left:2px}
.intro p{font-size:12px;line-height:24px;color:#333;margin-top:18px}
.btn-read{left:100px;top:910px;width:77px;height:29px;background:var(--blue);color:#fff;font-size:12px;font-weight:600;text-align:center;line-height:29px}

.rating{left:610px;top:728px}
.rating-text{left:708px;top:781px;color:#fff}
.rating-text b{font-size:17px;font-weight:600;display:block}
.rating-text small{font-size:7.5px}

.footer{left:0;top:1018px;width:952px;height:146px;background:var(--footer)}
.fcol{position:absolute;top:22px}
.fcol h4{font-size:12px;font-weight:600;color:#111;margin-bottom:9px}
.fcol p{font-size:7.5px;color:#555;line-height:14.5px}
.fcol .more{font-size:7.5px;font-weight:600;color:#1a8f5a;margin-top:6px;display:block}
.contact-line{display:flex;gap:8px;font-size:7.5px;color:#555;line-height:16px}
.contact-line .ic{width:6px;display:inline-flex;align-items:center}
.social{display:flex;align-items:center;gap:10px;font-size:10px;color:#333;height:18.5px}
.social i{width:15px;height:15px;display:inline-block}
.copy{left:0;top:1164px;width:952px;height:36px;background:var(--blue);color:#fff;font-size:9.5px;text-align:center;line-height:36px}
</style>
</head>
<body>

<div class="abs brand">
  <span class="brand-dot"></span>
  <span class="brand-name">Pine Grove Loan Aid</span>
</div>

<div class="abs top-contact">
  <div class="label">
    <svg width="18" height="18" viewBox="0 0 18 18"><rect width="18" height="18" rx="3" fill="#1a7fc1"/><path d="M5 4c1-.5 2 0 2.4 1l.5 1.4c.2.6-.1 1-.6 1.4.6 1.3 1.6 2.3 2.9 2.9.4-.5.8-.8 1.4-.6l1.4.5c1 .4 1.5 1.4 1 2.4-.5 1-1.6 1.4-2.6 1C8.6 12.6 5.4 9.4 4 6.6 3.6 5.6 4 4.5 5 4z" fill="#fff"/></svg>
    Contact Us
  </div>
  <div class="phone">012-555-0142</div>
</div>

<nav class="abs nav">
  <a class="active" href="#">Home</a>
  <a href="#">Debt Consolidation</a>
  <a href="#">About Us</a>
  <a href="#">Contact Us</a>
  <div class="login">
    <svg width="10" height="12" viewBox="0 0 10 12"><path d="M2.5 5V3.5a2.5 2.5 0 015 0V5" fill="none" stroke="#1a7fc1" stroke-width="1.5"/><rect x="0.5" y="5" width="9" height="7" rx="1" fill="#1a7fc1"/></svg>
    Log in
  </div>
</nav>

<div class="abs hero" role="img" aria-label="Photo of a financial advisor with a tablet talking with a smiling couple at a café table"></div>
<svg class="abs" style="left:574px;top:260px" width="16" height="30" viewBox="0 0 16 30"><path d="M3 2l10 13L3 28" fill="none" stroke="#ccc" stroke-width="3"/></svg>
<div class="abs hero-dots"><i></i><i class="on"></i><i></i><i></i></div>
<div class="abs hero-shadow"></div>

<svg class="abs lead-tab" width="256" height="8" viewBox="0 0 256 8"><path d="M0 8L6 0h244l6 8z" fill="#0b6ab8"/></svg>
<form class="abs lead">
  <h2>Our Debt Solutions<br>Can Help You</h2>
  <hr>
  <div class="field" style="left:24px;top:94px;width:242px;width:194px">Name</div>
  <div class="field" style="left:24px;top:130px;width:91px">Phone</div>
  <div class="field" style="left:121px;top:130px;width:96px">Email</div>
  <div class="field" style="left:24px;top:162px;width:91px">State<span class="caret"></span></div>
  <div class="field" style="left:121px;top:162px;width:96px">Debt Amount<span class="caret"></span></div>
  <div class="cta">Get Assistance Now</div>
</form>

<section class="abs card" style="left:100px">
  <h3>Act now to take advantage of<br>the following benefits</h3>
  <ul class="benefits">
    <li><svg width="9" height="8" viewBox="0 0 9 8"><path d="M1 4l2.5 2.5L8 1" fill="none" stroke="#b5103c" stroke-width="2"/></svg>Reduce high interest credit rates</li>
    <li><svg width="9" height="8" viewBox="0 0 9 8"><path d="M1 4l2.5 2.5L8 1" fill="none" stroke="#b5103c" stroke-width="2"/></svg>Stop harassing credit calls</li>
    <li><svg width="9" height="8" viewBox="0 0 9 8"><path d="M1 4l2.5 2.5L8 1" fill="none" stroke="#b5103c" stroke-width="2"/></svg>One low monthly payment</li>
    <li><svg width="9" height="8" viewBox="0 0 9 8"><path d="M1 4l2.5 2.5L8 1" fill="none" stroke="#b5103c" stroke-width="2"/></svg>No costs unless you save</li>
  </ul>
</section>
<div class="abs card-shadow" style="left:100px"></div>

<section class="abs card" style="left:356px">
  <h3>Current Debt Relief News</h3>
  <div class="news" style="top:30px">
    <div class="date">July<b>26</b></div>
    <div><div class="t">Credit Debt Relief: Understand Your Options</div>
    <p>Credit debt relief can be achieved in a number of ways. Generally, this may involve debt consolidation, debt settlement, bankruptcy and credit counseling....<br><span>[Read more]</span></p></div>
  </div>
  <div class="news" style="top:98px">
    <div class="date">July<b>26</b></div>
    <div><div class="t">Credit Debt Relief: Understand Your Options</div>
    <p>Credit debt relief can be achieved in a number of ways. Generally, this may involve debt consolidation, debt settlement, bankruptcy and credit counseling....<br><span>[Read more]</span></p></div>
  </div>
</section>
<div class="abs card-shadow" style="left:356px"></div>

<section class="abs card" style="left:611px">
  <h3>Recent Articles</h3>
  <div class="articles">
    •Non Profit Credit Counseling: Important Facts<br>
    •Credit Counseling: Getting Help to Manage Your<br>
    •Debts the Professional Way<br>
    •Managing Debts: Could Credit Counseling Services Help You?
  </div>
  <div class="see-more">See More</div>
</section>
<div class="abs card-shadow" style="left:611px"></div>

<article class="abs intro">
  <h2>When To Consider A Debt Consolidation Program</h2>
  <p>In today’s economy, it is very common for consumer’s to find themselves overwhelmed by credit card debt and in need of debt reduction. Consumers who need more than basic budgeting to pay off debts and are having difficulties making their monthly payments should consider a debt consolidation program in order to get back on track.</p>
</article>
<div class="abs btn-read">Read More</div>

<svg class="abs rating" width="242" height="165" viewBox="0 0 242 165">
  <path d="M3 3h237v162L5 150z" fill="#b5103c"/>
  <path d="M0 0h237v163L2 148z" fill="#0b7bd0"/>
  <rect x="36" y="27" width="56" height="87" fill="#fff" stroke="#d0d0d0"/>
  <rect x="40" y="31" width="48" height="79" fill="#1f6c8a"/>
</svg>
<div class="abs rating-text"><b>QFR Rating : A+</b><small>Click for review</small></div>

<footer class="abs footer">
  <div class="fcol" style="left:191px;width:170px">
    <h4>About our Company</h4>
    <p>Lorem ipsum dolor sit amet, consectetur adipiscing elit. Duis dapibus rhoncus purus, quis aliquet urna vehicula eu. Maecenas velit orci, volutpat sed posuere eu, vehicula eu tellus.</p>
    <span class="more">Learn more »</span>
  </div>
  <div class="fcol" style="left:452px">
    <h4>Contact Information</h4>
    <div class="contact-line"><span class="ic"><svg width="7" height="6" viewBox="0 0 7 6"><path d="M0 3L3.5 0 7 3H6v3H1V3z" fill="#333"/></svg></span>Dana R. Holt</div>
    <div class="contact-line"><span class="ic"></span>48 Harbour Lane</div>
    <div class="contact-line"><span class="ic"></span>Westfield, WF2 7QL</div>
    <div class="contact-line"><span class="ic"><svg width="5" height="7" viewBox="0 0 5 7"><rect x=".5" y=".5" width="4" height="6" rx=".5" fill="none" stroke="#333"/></svg></span>0845 000 4821</div>
    <div class="contact-line"><span class="ic"><svg width="7" height="5" viewBox="0 0 7 5"><rect width="7" height="5" fill="#333"/><path d="M0 0l3.5 3L7 0" fill="none" stroke="#ddd" stroke-width=".6"/></svg></span>hello@pinegroveloanaid.com</div>
  </div>
  <div class="fcol" style="left:670px">
    <h4>Follow Us</h4>
    <div class="social"><i style="background:#1d75b3"></i>Linkfolio</div>
    <div class="social"><i style="background:#2aa8e0"></i>Chirper</div>
    <div class="social"><i style="background:#3b5a9a"></i>Facepage</div>
    <div class="social"><i style="background:#d8452f"></i>PlusCircle</div>
  </div>
</footer>
<div class="abs copy">Copyright©Pine Grove Loan Aid 2014. All Rights Reserved.</div>

</body>
</html>
```